Charity donation cards

I need a card in an envelope that would be given out to people and they would put their donations along with their details (name and email) and give it back to us (dropped in acrylic boxes at events etc).

The card should be a medium size, bi or tri fold to be able to fit all the information i require.

The Sarwa Fund

The Bright Meadow Centre is dedicated to providing the much needed support to families and children struggling with their differences through a holistic and comprehensive approach that includes detailed evaluations, therapy programs and support services to help unlock the potential in every child.

We are so proud to be able to help empower our society by dedicating our business to the mental, physical and social well being of our younger community and pledging all our net profits to help ensure no child is ever left behind.

Professional services can often be expensive. Our Sarwa Fund helps support families requiring financial aid. We believe every child deserves the opportunity to succeed and no child should be left behind.

How can you help?

Gift the therapies to the children that need it the most. We welcome new sponsors, appreciate your gifts and gratefully accept your contributions as we expand to increase the number of children we can serve.

Name:
Email:
Amount:

We accept cash, checks or credit card payments at The Bright Meadow Centre.

Gift cards should be dropped in the designated acrylic boxes at TBMC or the event.

Please email sarwafund@tbmc-example.ae for more information on the process.
Http://www.tbmc-example.ae

Target Market(s)

These cards will be placed in the reception for our clients to donate.

We will also be working with party planners. Some parents don't want people to get them gifts for their kids birthday party so they want to use this instead.

Industry/Entity Type

Charity

Requirements
Must have
• The same feel as our centre Http://www.tbmc-example.ae
• our website, email and contact number
Nice to have
• Go to our website and feel free to take ideas and content.
• The design should be clean and simple.
• High light the key words in the text with bold and maybe in green to make it pop out.
Should not have
• Do not use the word donate in any print material. The word should be gift.

```html
<!DOCTYPE html>
<html lang="en">
<head>
<meta charset="utf-8">
<title>The Sarwa Fund – Gift Card</title>
<link href="https://fonts.googleapis.com/css2?family=Roboto:wght@300;400;700&family=Roboto+Condensed:wght@400;700&display=swap" rel="stylesheet">
<style>
  :root {
    --page: #ffffff;
    --card-edge: #d8d8d8;
    --card-face: #ebebeb;
    --ink: #3a3a3a;
    --fold: #8a8a8a;
    --rule: #b5b5b5;
    --name-ink: #5a5a5a;
  }
  * { margin: 0; padding: 0; box-sizing: border-box; }
  html, body { width: 1200px; height: 1000px; overflow: hidden; background: var(--page); }
  .canvas { position: relative; width: 1200px; height: 1000px; font-family: "Roboto Condensed", "Arial Narrow", sans-serif; color: var(--ink); }
  .card-shapes { position: absolute; left: 0; top: 0; }

  .help-title { position: absolute; left: 193px; top: 351px; width: 120px; text-align: center;
    font-family: "Roboto", Arial, sans-serif; font-weight: 700; font-size: 20px; line-height: 24px; color: var(--ink); }

  .help-copy { position: absolute; left: 337px; top: 368px; width: 236px; font-size: 9px; line-height: 11px; color: var(--ink); }
  .help-copy .ln { display: block; white-space: nowrap; text-align: justify; text-align-last: justify; }
  .help-copy .ln.last { text-align-last: left; }

  .details-form { position: absolute; left: 601px; top: 349px; width: 258px; font-size: 10px; color: var(--ink); }
  .form-row { display: flex; align-items: flex-end; height: 17px; }
  .form-row .label { white-space: nowrap; padding-right: 4px; }
  .form-row .line { flex: 1; border-bottom: 1px dashed var(--rule); margin-bottom: 3px; }
  .payment-note { margin-top: 5px; line-height: 12px; white-space: nowrap; }

  .drop-note { position: absolute; left: 878px; top: 353px; width: 112px; text-align: center;
    font-size: 10px; line-height: 12px; color: var(--ink); }

  .centre-name { position: absolute; left: 196px; top: 612px; width: 190px;
    font-family: "Roboto", Arial, sans-serif; font-weight: 300; font-size: 20px; line-height: 24px; color: var(--name-ink); }

  .contact { position: absolute; left: 597px; top: 626px; width: 263px; text-align: center;
    font-size: 10.5px; line-height: 12px; color: var(--ink); }
  .contact strong { font-weight: 700; }
</style>
</head>
<body>
<div class="canvas">
  <svg class="card-shapes" width="1200" height="1000" viewBox="0 0 1200 1000">
    <defs>
      <linearGradient id="logoFace" x1="0" y1="0" x2="0" y2="1">
        <stop offset="0" stop-color="#ffffff"/>
        <stop offset="1" stop-color="#f0f0f0"/>
      </linearGradient>
      <linearGradient id="contactPanel" x1="0" y1="0" x2="1" y2="0">
        <stop offset="0" stop-color="#a6a6a6"/>
        <stop offset="0.5" stop-color="#c9c9c9"/>
        <stop offset="1" stop-color="#b3b3b3"/>
      </linearGradient>
      <linearGradient id="classroomPhoto" x1="0" y1="0" x2="1" y2="0">
        <stop offset="0" stop-color="#f4f4f4" stop-opacity="0"/>
        <stop offset="0.25" stop-color="#c8cac6"/>
        <stop offset="0.5" stop-color="#3f5a45"/>
        <stop offset="0.8" stop-color="#8a5a3e"/>
        <stop offset="1" stop-color="#6e2e22"/>
      </linearGradient>
      <radialGradient id="glitterPhoto" cx="0.5" cy="0.55" r="0.6">
        <stop offset="0" stop-color="#d9b39a"/>
        <stop offset="0.6" stop-color="#b98f7c"/>
        <stop offset="1" stop-color="#7d8ea0"/>
      </radialGradient>
    </defs>

    <line x1="594" y1="313" x2="594" y2="470" stroke="var(--fold)" stroke-dasharray="3 3"/>
    <line x1="594" y1="558" x2="594" y2="715" stroke="var(--fold)" stroke-dasharray="3 3"/>

    <g class="card-inside">
      <circle cx="250" cy="389" r="85" fill="var(--card-edge)"/>
      <circle cx="935" cy="389" r="85" fill="var(--card-edge)"/>
      <rect x="300" y="340" width="590" height="98" fill="var(--card-edge)"/>
      <circle cx="250" cy="389" r="79" fill="var(--card-face)"/>
      <circle cx="935" cy="389" r="79" fill="var(--card-face)"/>
      <rect x="305" y="346" width="580" height="86" fill="var(--card-face)"/>
    </g>

    <g class="card-outside">
      <circle cx="250" cy="636" r="85" fill="var(--card-edge)"/>
      <circle cx="935" cy="636" r="85" fill="var(--card-edge)"/>
      <rect x="300" y="587" width="590" height="98" fill="var(--card-edge)"/>
      <circle cx="250" cy="636" r="79" fill="url(#logoFace)"/>
      <rect x="305" y="594" width="290" height="84" fill="url(#logoFace)"/>
      <rect x="330" y="594" width="260" height="84" fill="url(#classroomPhoto)" role="img" aria-label="Photo of a smiling girl writing on a green chalkboard"/>
      <rect x="597" y="594" width="288" height="84" fill="url(#contactPanel)"/>
      <circle cx="935" cy="636" r="79" fill="#ffffff"/>
      <circle cx="933" cy="636" r="77" fill="url(#glitterPhoto)" role="img" aria-label="Photo of a child blowing glitter from cupped hands"/>
    </g>
  </svg>

  <h2 class="help-title">How<br>can you<br>help?</h2>

  <p class="help-copy">
    <span class="ln">Gift the therapies to the children that need it the most. We</span>
    <span class="ln">welcome new sponsors, appreciate your gifts and gratefully</span>
    <span class="ln">accept your contributions as we expand to increase the</span>
    <span class="ln last">number of children we can serve.</span>
  </p>

  <div class="details-form">
    <div class="form-row"><span class="label">Name:</span><span class="line"></span></div>
    <div class="form-row"><span class="label">Email:</span><span class="line"></span></div>
    <div class="form-row"><span class="label">Amount:</span><span class="line"></span></div>
    <p class="payment-note">We accept cash, checks or credit card payments<br>at The Bright Meadow Centre.</p>
  </div>

  <p class="drop-note">Gift cards<br>should be dropped in<br>the designated<br>acrylic boxes at<br>TBMC or<br>the event.</p>

  <p class="centre-name">The Bright Meadow<br>Centre</p>

  <p class="contact">Email - <strong>sarwafund@tbmc-example.ae</strong><br>Web - <strong>www.tbmc-example.ae</strong></p>
</div>
</body>
</html>
```